INFOGRAPHIC DESING GYM SCHEDULE . FULL SCHEDULE AND CLASSES ROON SCHEDULE

I NEED TO CREATED A DESIGN FOR COMPLETE SCHEDULE TAMPLE FOR OUR GYM
AND SMALL SCHEDULE FOR EACH ROON OF THE GYM AND THE CLASSES THTA HAPPEN IN THE ROON
THE SCHEDULE WILL HAVE
CLASSES SCHEDULE
CLASSE DESCRIPTION
AND GRAPHIC EXPLAN HOW EFFECTIVE THE CLASSES ARE IN SOME IMPORT FECTOR .
I MAKE MY SELF A SAMPLE AND WILL UP LOAD IT NO WEEL DONE, BUT YOU CAN HAVE AN IDEIA
II LIKE TO MAKE IT BETTER AND MORE PROFESSIONAL .
RIGHT NOW WE CAN HAVE ALL AS PLACE HOLDER
Updates

hello i never got any other file right now i am very frustrated with this servese i spend a lot of monet for a design this experience is far from been good

Target Market(s)

gym

Font styles to use
Sans Serif

Colors
ec1f27
000000
9d9d9d

Requirements
Must have
• MUST HAVE A UNIQUE DESIGN . WILL USE ALL OF OUR GYM AND WILL NEED TO HAVE A PERSOLIZED DESIGN .
• WE NEED TO HAVE A TAMPLE WHERE WE CAN CHAGE OUR SELF BECOUSE THE CLASSE SCHEDULE CHANGE OTHER TIME
Nice to have
• THE GRAFIC EXPLAN HOW EFECTIVE THE CLASSES ARE IN EXTREMILY IMPORTANT. WE WANT TO INOVAT AND CRETED SOMETIMNH UNIQUE
• I UP LOAD OUR LOGO, IS SHOULD TO FOLOW OUR COLORS
• ON THE SCHEDUDLE SHOULD HAVE A LOGO

```html
<!DOCTYPE html>
<html lang="en">
<head>
<meta charset="utf-8">
<title>Gym Room Schedules</title>
<link rel="stylesheet" href="https://fonts.googleapis.com/css2?family=Roboto:wght@400;500;700;900&display=swap">
<style>
:root{
  --red:#ec1f27;
  --red-soft:#f0604f;
  --red-pale:#f3a9a2;
  --grey:#9d9d9d;
  --grey-dark:#7a7a7a;
  --ink:#1a1a1a;
  --panel-top:#333b42;
  --panel-bottom:#1b2025;
  --cyan:#27a9e1;
  --paper:#ffffff;
  --wall:#e4e4e4;
}
*{box-sizing:border-box;margin:0;padding:0}
html,body{width:1200px;height:827px;overflow:hidden}
body{background:var(--wall);font-family:"Roboto",Arial,sans-serif;color:var(--ink);position:relative}

.poster{position:absolute;top:110px;width:466px;height:640px;background:var(--paper);display:flex;flex-direction:column;align-items:stretch;padding:10px 0 0}
.poster--bike{left:87px}
.poster--fitness{left:647px}

/* header banner */
.banner{position:relative;margin:0 10px;height:84px;background:linear-gradient(180deg,#f0535a,var(--red));color:#fff;text-align:center;padding-top:12px}
.banner::after{content:"";position:absolute;left:50%;bottom:-14px;transform:translateX(-50%);border-left:22px solid transparent;border-right:22px solid transparent;border-top:14px solid var(--red)}
.banner__title{font-size:40px;font-weight:700;line-height:1;letter-spacing:.5px}
.banner__sub{font-size:10px;font-weight:500;letter-spacing:9px;margin-top:6px}

/* legend */
.legend{display:flex;justify-content:center;gap:110px;margin-top:24px;font-size:6px;font-weight:500}
.legend__item{display:flex;align-items:center;gap:14px}
.legend__dot{width:10px;height:10px;border-radius:50%}
.legend__item--am{color:var(--red)}
.legend__item--am .legend__dot{background:var(--red)}
.legend__item--pm{color:var(--grey-dark)}
.legend__item--pm .legend__dot{background:var(--grey)}

/* schedule */
.schedule{margin:14px 20px 0;display:grid;grid-template-columns:48px repeat(6,1fr);row-gap:6px;align-items:center;text-align:center}
.schedule__head{font-size:7px;font-weight:700;padding-bottom:6px}
.time{display:flex;align-items:baseline;justify-content:center;font-weight:700}
.time__hour{font-size:29px;line-height:1}
.time__min{font-size:8px}
.slot{font-size:6.3px;font-weight:700;line-height:1.25}
.morning{color:var(--red)}
.afternoon{color:var(--grey)}
.dash{display:block;width:22px;height:1px;background:currentColor;margin:0 auto}

/* definitions panel */
.definitions{position:relative;margin:18px 0 0;background:linear-gradient(180deg,var(--panel-top),var(--panel-bottom));color:#fff;padding:12px 16px 16px}
.definitions::after{content:"";position:absolute;left:50%;bottom:-13px;transform:translateX(-50%);border-left:20px solid transparent;border-right:20px solid transparent;border-top:13px solid var(--panel-bottom)}
.definitions__title{text-align:center;font-size:14px;font-weight:700;letter-spacing:.3px}
.definitions__list{display:flex;justify-content:space-around;gap:10px;margin-top:12px}
.class-def{flex:1;text-align:center}
.class-def__name{color:var(--cyan);font-size:11px;font-weight:700}
.class-def__text{font-size:5.2px;line-height:1.35;margin-top:6px}
.definitions--five .class-def__name{font-size:9px}
.definitions--five .class-def__text{font-size:5.2px;padding:0 4px}

/* intensity */
.intensity__title{text-align:center;font-size:14px;font-weight:700;margin-top:26px}
.intensity{margin:12px 22px 0;display:grid;grid-template-columns:62px repeat(8,1fr);row-gap:8px;align-items:center;text-align:center;font-size:6.2px;font-weight:700}
.intensity--five{row-gap:6px}
.intensity__label{text-align:center;color:var(--ink)}
.intensity__head{color:var(--ink)}
.lvl-high{color:var(--red)}
.lvl-median{color:var(--red-soft)}
.lvl-low{color:var(--red-pale)}

/* footer */
.footer{margin:auto 22px 22px;display:flex;align-items:flex-end;gap:12px}
.brand{display:flex;align-items:center;gap:6px;font-size:8px;font-weight:700;color:#4a4a4a;width:120px}
.brand__mark{width:22px;height:22px;border-radius:50%;background:var(--red);flex:none}
.feature{font-size:5px;font-weight:700;border-top:1px solid var(--ink);padding-top:3px;width:60px}
.dryness{flex:1;font-size:5px;font-weight:500;color:var(--grey-dark)}
.dryness__labels{display:flex;justify-content:space-between;padding:0 2px 2px}
.dryness__bar{height:8px;border:1px solid var(--ink);background:linear-gradient(90deg,#fff 0 25%,#f7e27a 25% 45%,#f5b04a 45% 65%,#ee7a3a 65% 85%,var(--red) 85%)}
</style>
</head>
<body>

<section class="poster poster--bike" aria-label="Bike room schedule">
  <header class="banner">
    <h1 class="banner__title">BIKE ROOM</h1>
    <p class="banner__sub">SCHEDULE</p>
  </header>
  <div class="legend">
    <span class="legend__item legend__item--am"><i class="legend__dot"></i>MORNING SCHEDULE</span>
    <span class="legend__item legend__item--pm"><i class="legend__dot"></i>AFTERNOON SCHEDULE</span>
  </div>
  <div class="schedule">
    <span class="schedule__head">TIME</span><span class="schedule__head">MONDAY</span><span class="schedule__head">TUESDAY</span><span class="schedule__head">WEDNESDAY</span><span class="schedule__head">THURSDAY</span><span class="schedule__head">FRIDAY</span><span class="schedule__head">SATURDAY</span>

    <span class="time morning"><b class="time__hour">8</b><span class="time__min">:30</span></span>
    <span class="slot morning">SAW</span><span class="slot morning">HIT<br>CYCLING</span><span class="slot morning">SAW</span><span class="slot morning">HIT<br>CYCLING</span><span class="slot morning">SAW</span><span class="slot morning"><i class="dash"></i></span>

    <span class="time morning"><b class="time__hour">9</b><span class="time__min">:30</span></span>
    <span class="slot morning">INDOOR<br>CYCLING</span><span class="slot morning">SAW</span><span class="slot morning">INDOOR<br>CYCLING</span><span class="slot morning">SAW</span><span class="slot morning">INDOOR<br>CYCLING</span><span class="slot morning">SAW</span>

    <span class="time afternoon"><b class="time__hour">5</b><span class="time__min">:30</span></span>
    <span class="slot afternoon">HIT<br>CYCLING</span><span class="slot afternoon">SAW</span><span class="slot afternoon">HIT<br>CYCLING</span><span class="slot afternoon">SAW</span><span class="slot afternoon">HIT<br>CYCLING</span><span class="slot afternoon"><i class="dash"></i></span>

    <span class="time afternoon"><b class="time__hour">6</b><span class="time__min">:30</span></span>
    <span class="slot afternoon">SAW</span><span class="slot afternoon">INDOOR<br>CYCLING</span><span class="slot afternoon">SAW</span><span class="slot afternoon">INDOOR<br>CYCLING</span><span class="slot afternoon">SAW</span><span class="slot afternoon"><i class="dash"></i></span>
  </div>

  <section class="definitions">
    <h2 class="definitions__title">CLASSES DEFINITION</h2>
    <div class="definitions__list">
      <div class="class-def"><h3 class="class-def__name">SAW</h3><p class="class-def__text">KIDS BOXING CLASS TEACHES BASIC BOXING SKILLS AND TECHNIQUES SUCH AS; STANCE, GUARD, MOVEMENT, JAB, CROSS, HOOK. IT INCREASES STRENGTH AND IMPROVES ENDURANCE.</p></div>
      <div class="class-def"><h3 class="class-def__name">HIT CYCLING</h3><p class="class-def__text">KIDS BOXING CLASS TEACHES BASIC BOXING SKILLS AND TECHNIQUES SUCH AS; STANCE, GUARD, MOVEMENT, JAB, CROSS, HOOK. IT INCREASES STRENGTH AND IMPROVES ENDURANCE.</p></div>
      <div class="class-def"><h3 class="class-def__name">INDOOR CYCLING</h3><p class="class-def__text">KIDS BOXING CLASS TEACHES BASIC BOXING SKILLS AND TECHNIQUES SUCH AS; STANCE, GUARD, MOVEMENT, JAB, CROSS, HOOK. IT INCREASES STRENGTH AND IMPROVES ENDURANCE.</p></div>
    </div>
  </section>

  <h2 class="intensity__title">CLASSES FINTENSITY</h2>
  <div class="intensity">
    <span></span><span class="intensity__head">FAT BURN</span><span class="intensity__head">INTENSITY</span><span class="intensity__head">CARDIO</span><span class="intensity__head">AGILITY</span><span class="intensity__head">BALANCE</span><span class="intensity__head">FLEXIBILITY</span><span class="intensity__head">POWER</span><span class="intensity__head">CONTACT</span>

    <span class="intensity__label">SAW</span>
    <span class="lvl-high">HIGH</span><span class="lvl-high">HIGH</span><span class="lvl-high">HIGH</span><span class="lvl-high">HIGH</span><span class="lvl-median">MEDIAN</span><span class="lvl-median">MEDIAN</span><span class="lvl-median">MEDIAN</span><span class="lvl-low">LOW</span>

    <span class="intensity__label">HIT<br>CYCLING</span>
    <span class="lvl-high">HIGH</span><span class="lvl-high">HIGH</span><span class="lvl-high">HIGH</span><span class="lvl-median">MEDIAN</span><span class="lvl-median">MEDIAN</span><span class="lvl-median">MEDIAN</span><span class="lvl-low">LOW</span><span class="lvl-low">LOW</span>

    <span class="intensity__label">INDOOR<br>CYCLING</span>
    <span class="lvl-high">HIGH</span><span class="lvl-median">MEDIAN</span><span class="lvl-median">MEDIAN</span><span class="lvl-median">MEDIAN</span><span class="lvl-low">LOW</span><span class="lvl-low">LOW</span><span class="lvl-low">LOW</span><span class="lvl-low">LOW</span>
  </div>

  <footer class="footer">
    <div class="brand"><span class="brand__mark"></span>SUMMIT TRAINING CENTER</div>
    <div class="feature">WATERPROOFING</div>
    <div class="feature">DRYSHELL</div>
    <div class="dryness">
      <div class="dryness__labels"><span>DRY</span><span>VERY DRY</span></div>
      <div class="dryness__bar"></div>
    </div>
  </footer>
</section>

<section class="poster poster--fitness" aria-label="Fitness room schedule">
  <header class="banner">
    <h1 class="banner__title">FITNESS ROOM</h1>
    <p class="banner__sub">SCHEDULE</p>
  </header>
  <div class="legend">
    <span class="legend__item legend__item--am"><i class="legend__dot"></i>MORNING SCHEDULE</span>
    <span class="legend__item legend__item--pm"><i class="legend__dot"></i>AFTERNOON SCHEDULE</span>
  </div>
  <div class="schedule">
    <span class="schedule__head">TIME</span><span class="schedule__head">MONDAY</span><span class="schedule__head">TUESDAY</span><span class="schedule__head">WEDNESDAY</span><span class="schedule__head">THURSDAY</span><span class="schedule__head">FRIDAY</span><span class="schedule__head">SATURDAY</span>

    <span class="time morning"><b class="time__hour">8</b><span class="time__min">:30</span></span>
    <span class="slot morning">HITT</span><span class="slot morning">CROSS CIRCUIT</span><span class="slot morning">HITT</span><span class="slot morning">CROSS CIRCUIT</span><span class="slot morning">HITT</span><span class="slot morning"><i class="dash"></i></span>

    <span class="time afternoon"><b class="time__hour">4</b><span class="time__min">:30</span></span>
    <span class="slot afternoon">KIDS FITNESS</span><span class="slot afternoon">TEEN FITNESS</span><span class="slot afternoon">KIDS FITNESS</span><span class="slot afternoon">TEEN FITNESS</span><span class="slot afternoon">KIDS FITNESS</span><span class="slot afternoon"><i class="dash"></i></span>

    <span class="time afternoon"><b class="time__hour">5</b><span class="time__min">:30</span></span>
    <span class="slot afternoon">SUMMIT<br>BOOT CAMP</span><span class="slot afternoon">FIGHT<br>FITNESS</span><span class="slot afternoon">SUMMIT<br>BOOT CAMP</span><span class="slot afternoon">FIGHT<br>FITNESS</span><span class="slot afternoon">SUMMIT<br>BOOT CAMP</span><span class="slot afternoon"><i class="dash"></i></span>

    <span class="time afternoon"><b class="time__hour">6</b><span class="time__min">:30</span></span>
    <span class="slot afternoon">CROSS CIRCUIT</span><span class="slot afternoon">HITT</span><span class="slot afternoon">CROSS CIRCUIT</span><span class="slot afternoon">HITT</span><span class="slot afternoon">CROSS CIRCUIT</span><span class="slot afternoon"><i class="dash"></i></span>
  </div>

  <section class="definitions definitions--five">
    <h2 class="definitions__title">CLASSES DEFINITION</h2>
    <div class="definitions__list">
      <div class="class-def"><h3 class="class-def__name">HITT</h3><p class="class-def__text">KIDS BOXING CLASS TEACHES BASIC BOXING SKILLS AND TECHNIQUES SUCH AS; STANCE, GUARD, MOVEMENT, JAB, CROSS, HOOK. IT INCREASES STRENGTH AND IMPROVES ENDURANCE.</p></div>
      <div class="class-def"><h3 class="class-def__name">BOOT CAMP</h3><p class="class-def__text">KIDS BOXING CLASS TEACHES BASIC BOXING SKILLS AND TECHNIQUES SUCH AS; STANCE, GUARD, MOVEMENT, JAB, CROSS, HOOK. IT INCREASES STRENGTH AND IMPROVES ENDURANCE.</p></div>
      <div class="class-def"><h3 class="class-def__name">CROSS CIRCUIT</h3><p class="class-def__text">KIDS BOXING CLASS TEACHES BASIC BOXING SKILLS AND TECHNIQUES SUCH AS; STANCE, GUARD, MOVEMENT, JAB, CROSS, HOOK. IT INCREASES STRENGTH AND IMPROVES ENDURANCE.</p></div>
      <div class="class-def"><h3 class="class-def__name">TEEN FITNESS</h3><p class="class-def__text">KIDS BOXING CLASS TEACHES BASIC BOXING SKILLS AND TECHNIQUES SUCH AS; STANCE, GUARD, MOVEMENT, JAB, CROSS, HOOK. IT INCREASES STRENGTH AND IMPROVES ENDURANCE.</p></div>
      <div class="class-def"><h3 class="class-def__name">KIDS FITNESS</h3><p class="class-def__text">KIDS BOXING CLASS TEACHES BASIC BOXING SKILLS AND TECHNIQUES SUCH AS; STANCE, GUARD, MOVEMENT, JAB, CROSS, HOOK. IT INCREASES STRENGTH AND IMPROVES ENDURANCE.</p></div>
    </div>
  </section>

  <h2 class="intensity__title">CLASSES FINTENSITY</h2>
  <div class="intensity intensity--five">
    <span></span><span class="intensity__head">FAT BURN</span><span class="intensity__head">INTENSITY</span><span class="intensity__head">CARDIO</span><span class="intensity__head">AGILITY</span><span class="intensity__head">BALANCE</span><span class="intensity__head">FLEXIBILITY</span><span class="intensity__head">POWER</span><span class="intensity__head">CONTACT</span>

    <span class="intensity__label">SAW</span>
    <span class="lvl-high">HIGH</span><span class="lvl-high">HIGH</span><span class="lvl-high">HIGH</span><span class="lvl-high">HIGH</span><span class="lvl-median">MEDIAN</span><span class="lvl-median">MEDIAN</span><span class="lvl-low">LOW</span><span class="lvl-low">LOW</span>

    <span class="intensity__label">BOOT CAMP</span>
    <span class="lvl-high">HIGH</span><span class="lvl-high">HIGH</span><span class="lvl-high">HIGH</span><span class="lvl-high">HIGH</span><span class="lvl-high">HIGH</span><span class="lvl-median">MEDIAN</span><span class="lvl-median">MEDIAN</span><span class="lvl-low">LOW</span>

    <span class="intensity__label">CROSS CIRCUIT</span>
    <span class="lvl-high">HIGH</span><span class="lvl-high">HIGH</span><span class="lvl-high">HIGH</span><span class="lvl-high">HIGH</span><span class="lvl-high">HIGH</span><span class="lvl-median">MEDIAN</span><span class="lvl-high">HIGH</span><span class="lvl-low">LOW</span>

    <span class="intensity__label">TEEN FITNESS</span>
    <span class="lvl-median">MEDIAN</span><span class="lvl-median">MEDIAN</span><span class="lvl-median">MEDIAN</span><span class="lvl-high">HIGH</span><span class="lvl-high">HIGH</span><span class="lvl-median">MEDIAN</span><span class="lvl-low">LOW</span><span class="lvl-low">LOW</span>

    <span class="intensity__label">KIDS FITNESS</span>
    <span class="lvl-low">LOW</span><span class="lvl-low">LOW</span><span class="lvl-low">LOW</span><span class="lvl-high">HIGH</span><span class="lvl-median">MEDIAN</span><span class="lvl-median">MEDIAN</span><span class="lvl-low">LOW</span><span class="lvl-low">LOW</span>
  </div>

  <footer class="footer">
    <div class="brand"><span class="brand__mark"></span>SUMMIT TRAINING CENTER</div>
    <div class="feature">WATERPROOFING</div>
    <div class="feature">DRYSHELL</div>
    <div class="dryness">
      <div class="dryness__labels"><span>DRY</span><span>VERY DRY</span></div>
      <div class="dryness__bar"></div>
    </div>
  </footer>
</section>

</body>
</html>
```